Meditations CD Cover
Zielgruppe
Wir unterstützen Therapeuten ihre Praxis aufzubauen.
Aufgabenstellung
Ich wünsche einen CD Cover mit Rückseite und CD Druck, wo nicht zu esoterisch aussieht. Bitte keine Buddha, Steine, Yoga, Lotusblume!
ich hätte gerne mein Bild im Vordergrund, nicht zu prominent, klar strukturiert und nicht zu schwer, lieber mehr Platz lassen.
ich hätte gerne eine CD Jewel Cases.
Bitte eine ganz neutralle CD ohne das Grün von der Website. (sonnen-kern-werk.ch)
Die Meditation ist eine Mischung zwischen Business und Meditation, es geht um Kundenfindung.
Etwas schlichtes und modernes.
Was rauf muss:
CD Cover
Mirela Gantenbein-Rusch
Mein Foto
Titel:
Finde Deinen Kompass, Pfad der Stille!
bitte auch schreiben: die ÜBUNGS-CD zum Buch
Logo und mein Bild, nicht zu prominent!!!!
Beispiel: http://lunavertomiel.com/
http://www.bildquello.com/vector/electric-bulb-16125607?st=0561491
http://www.bildquello.com/vector/dart-board-16126309?st=425cf59
http://klangwiese-audio.com/tarnow-lukas-neue-pfade-zu-glueck-ruhe-und-freude-cd
Rückseite:
mein Foto und der Text:
Gehen Sie in die Resonanz und finden Sie den richtigen Klienten.
Gerne unterstütze ich Sie auf diesem wundervollen Weg ...
Mein Name ist Mirela Gantenbein, ich bin erfolgreiche Unternehmerin, die zugleich spiri- tuell denkt und handelt. Und ich bin fest davon überzeugt. Es gibt eine innere Kraft, die nicht nur Berge versetzt. Sondern auch Ihre Praxis fullt.
Auf dieser CD werden Sie angeleitet sich mit ihrem Idealkunden zu treffen. Sie werden entdecken welche Probleme oder Herausforderungen, Wünsche und Ziele Ihr potenzieller Klient.
Vielen Dank und viel Spass :-)

```html
<!DOCTYPE html>
<html lang="de">
<head>
<meta charset="utf-8">
<title>Finde Deinen Kompass – Übungs-CD</title>
<link href="https://fonts.googleapis.com/css2?family=Didact+Gothic&family=Poiret+One&family=Open+Sans:wght@700&display=swap" rel="stylesheet">
<style>
  :root {
    --page: #ffffff;
    --orange-light: #f6b25a;
    --orange: #e9893a;
    --orange-deep: #a8592a;
    --hex-fill: #f8e3d6;
    --ink: #2a2522;
    --photo-light: #e6e3e1;
    --photo-dark: #6d6a68;
    --spine: #ffffff;
  }
  * { margin: 0; padding: 0; box-sizing: border-box; }
  html, body {
    width: 1200px; height: 520px; overflow: hidden;
    background: var(--page);
    font-family: "Didact Gothic", sans-serif;
    color: var(--ink);
  }
  .canvas { position: relative; width: 1200px; height: 520px; }

  .back-cover { position: absolute; left: 44px; top: 0; width: 624px; height: 480px; background: var(--spine); box-shadow: 2px 6px 8px rgba(0,0,0,.25); }
  .front-cover { position: absolute; left: 694px; top: 0; width: 480px; height: 480px; box-shadow: 2px 6px 8px rgba(0,0,0,.25); }
  .panel-art { position: absolute; inset: 0; }
  .back-cover .panel-art { left: 32px; width: 561px; }

  .spine-text {
    position: absolute; top: 0; height: 480px; width: 32px;
    display: flex; align-items: center; justify-content: center;
    writing-mode: vertical-rl;
    font-family: "Open Sans", sans-serif; font-weight: 700; font-size: 10.5px;
  }
  .spine-left { left: 0; transform: rotate(180deg); }
  .spine-right { right: 0; }

  .back-text {
    position: absolute; left: 153px; top: 47px; width: 290px;
    font-size: 14.2px; line-height: 16.1px;
  }
  .back-text p { margin-bottom: 16px; }
  .back-text .thanks { margin-top: 32px; }

  .brand { position: absolute; display: flex; align-items: center; gap: 6px; font-family: "Didact Gothic", sans-serif; color: var(--ink); }
  .brand-dot { border-radius: 50%; background: var(--orange); }
  .back-brand { left: 196px; top: 428px; font-size: 22px; }
  .back-brand .brand-dot { width: 30px; height: 30px; }
  .front-brand { left: 309px; top: 114px; font-size: 16px; }
  .front-brand .brand-dot { width: 22px; height: 22px; }

  .cd-title {
    position: absolute; left: 80px; top: 200px; width: 330px; text-align: center;
    font-family: "Poiret One", sans-serif; font-size: 30px; line-height 37px; line-height: 38px;
  }
  .cd-author {
    position: absolute; left: 80px; top: 290px; width: 330px; text-align: center;
    font-family: "Open Sans", sans-serif; font-weight: 700; font-size: 12.5px;
  }
  .cd-subtitle {
    position: absolute; left: 21px; top: 398px;
    font-family: "Open Sans", sans-serif; font-weight: 700; font-size: 16.5px; line-height: 20px;
  }
</style>
</head>
<body>
<div class="canvas">

  <section class="back-cover">
    <div class="spine-text spine-left">Mirela Gantenbein-Rusch</div>
    <svg class="panel-art" viewBox="0 0 561 480" width="561" height="480">
      <defs>
        <linearGradient id="backGlow" x1="0" y1="0" x2="1" y2="0.3">
          <stop offset="0" stop-color="var(--orange-light)"/>
          <stop offset="0.55" stop-color="var(--orange)"/>
          <stop offset="1" stop-color="var(--orange-deep)"/>
        </linearGradient>
        <linearGradient id="backPhoto" x1="0" y1="0" x2="0" y2="1">
          <stop offset="0" stop-color="var(--photo-dark)"/>
          <stop offset="0.5" stop-color="var(--photo-light)"/>
          <stop offset="1" stop-color="var(--page)"/>
        </linearGradient>
      </defs>
      <rect width="561" height="480" fill="url(#backGlow)"/>
      <polygon points="140,0 418,0 557,240 418,480 140,480 3,240" fill="var(--hex-fill)" opacity="0.93"/>
      <path role="img" aria-label="Schwarz-Weiss-Porträt der Autorin in weisser Bluse" d="M303,480 C320,420 380,380 405,350 C395,300 400,230 445,205 C495,185 530,220 527,290 C522,330 520,350 561,400 L561,480 Z" fill="url(#backPhoto)"/>
    </svg>
    <div class="spine-text spine-right">Mirela Gantenbein-Rusch</div>

    <div class="back-text">
      <p>Gehen Sie in die Resonanz und<br>finden Sie den richtigen Klienten.<br>Gerne unterstütze ich Sie auf<br>diesem wundervollen Weg.</p>
      <p>Mein Name ist Mirela Gantenbein, ich<br>bin erfolgreiche Unternehmerin, die<br>zugleich spirituell denkt und handelt.<br>Und ich bin fest davon überzeugt.<br>Es gibt eine innere Kraft, die nicht<br>nur Berge versetzt. Sondern auch<br>Ihre Praxis füllt.</p>
      <p>Auf dieser CD werden Sie angeleitet<br>sich mit ihrem Idealkunden zu treffen.<br>Sie werden entdecken welche Probleme<br>oder Herausforderungen, Wünsche und<br>Ziele Ihr potenzieller Klient.</p>
      <p class="thanks">Vielen Dank und viel Spass</p>
    </div>

    <div class="brand back-brand"><span class="brand-dot"></span>NORVA</div>
  </section>

  <section class="front-cover">
    <svg class="panel-art" viewBox="0 0 480 480" width="480" height="480">
      <defs>
        <linearGradient id="frontGlow" x1="0" y1="0" x2="1" y2="0.4">
          <stop offset="0" stop-color="var(--orange-light)"/>
          <stop offset="0.55" stop-color="var(--orange)"/>
          <stop offset="1" stop-color="var(--orange-deep)"/>
        </linearGradient>
        <linearGradient id="frontPhoto" x1="0" y1="0" x2="0" y2="1">
          <stop offset="0" stop-color="var(--photo-dark)"/>
          <stop offset="0.55" stop-color="var(--photo-light)"/>
          <stop offset="1" stop-color="var(--page)"/>
        </linearGradient>
      </defs>
      <rect width="480" height="480" fill="url(#frontGlow)"/>
      <polygon points="182,98 379,98 475,266 379,436 182,436 86,266" fill="var(--hex-fill)" opacity="0.93"/>
      <path role="img" aria-label="Kleines Schwarz-Weiss-Porträt der Autorin" d="M223,436 C226,405 245,395 258,385 C250,360 250,335 270,328 C295,322 305,345 300,370 C298,380 302,390 320,400 C328,410 330,425 330,436 Z" fill="url(#frontPhoto)"/>
    </svg>

    <div class="brand front-brand"><span class="brand-dot"></span>NORVA</div>
    <h1 class="cd-title">Finde Deinen Kompass,<br>Pfad der Stille!</h1>
    <div class="cd-author">Mirela Gantenbein-Rusch</div>
    <div class="cd-subtitle">die ÜBUNGS-CD<br>zum Buch</div>
  </section>

</div>
</body>
</html>
```